Business card design for Tarvello Studios, and Event & Entertainment business

The business card design is for a new business venture, Tarvello Studios. This company offers Event management, entertainment management and also Latin dance tuition. We currently run Latin dance festivals in Australia & also teach street Latin. This business card is for the director, Wren Hollis. The Logo has already been designed. So, I need the new design to incorporate and go with the existing Logo.

The look I like is clean, simple & elegant but I also want it to be sexy. Elegant, but not corporate. Clean & simple but not boring :-)

If you want to add another design element as well as using the Logo, please use something with movement. I like ripples or swirls for example.

I would also like to have part of the card embossed or Spot UV pressed so I would like some part of the design to have texture.

Text for the Cards is as follows;

Tarvello Studios ( Logo attached )

Wren Hollis

EVENTS & ENTERTAINMENT MANAGEMENT

m: 0487 552 031
e: wren@tarvellostudios.com.au
f Tarvello Studios

www.tarvellostudios.com.au

Please try portrait layout.

Thanks, Wren
Updates

Hello Designers, Thank you to all of you who have submitted designs for Tarvello Studios. I will make up my mind now from what I have already been sent. Very close to making a decision :-) Thank you, Wren

Target Market(s)

Adults, 18 - 60 age group. People who are active. People interested in different cultures. People who like to travel. Please who like to have fun. People who are passionate about Latin dance.

Industry/Entity Type

Entertainment

Font styles to use
Sans Serif
Script

Colors
9bcb3c
ec1f27
ffffff

Requirements
Must have
• Logo + All text listed in brief
Nice to have
• An extra design feature or background image that could be embossed or spot uv pressed to add texture & flare.

```html
<!DOCTYPE html>
<html lang="en">
<head>
<meta charset="utf-8">
<title>Tarvello Studios – Business Card</title>
<link rel="stylesheet" href="https://fonts.googleapis.com/css2?family=Dancing+Script:wght@500&family=Mulish:wght@400;600&display=swap">
<style>
  :root {
    --page: #ffffff;
    --card: #2b2b2b;
    --card-edge: #262626;
    --ink: #ffffff;
    --ink-soft: #d9d9d9;
    --chilli: #ec1f27;
    --lime: #9bcb3c;
  }
  * { margin: 0; padding: 0; box-sizing: border-box; }
  html, body {
    width: 878px;
    height: 1200px;
    overflow: hidden;
    background: var(--page);
  }
  .sheet {
    position: relative;
    width: 878px;
    height: 1200px;
  }
  .card {
    position: absolute;
    left: 80px;
    width: 723px;
    height: 477px;
    background: radial-gradient(ellipse at 50% 40%, #303030 0%, var(--card) 55%, var(--card-edge) 100%);
    color: var(--ink);
    font-family: "Mulish", Arial, sans-serif;
  }
  .card--front { top: 77px; }
  .card--back { top: 637px; }

  /* Front */
  .brand {
    position: absolute;
    left: 0;
    right: 0;
    top: 175px;
    display: flex;
    justify-content: center;
    align-items: center;
    gap: 16px;
  }
  .brand__dot {
    width: 22px;
    height: 22px;
    border-radius: 50%;
    background: var(--chilli);
  }
  .brand__name {
    font-family: "Dancing Script", "Brush Script MT", cursive;
    font-weight: 500;
    font-size: 76px;
    line-height: 1;
    color: var(--ink);
  }
  .tagline {
    position: absolute;
    left: 0;
    right: 0;
    top: 322px;
    text-align: center;
    font-size: 12.5px;
    font-weight: 600;
    letter-spacing: 2.2px;
    color: var(--ink-soft);
  }

  /* Back */
  .brand-mini {
    position: absolute;
    left: 54px;
    top: 72px;
    font-family: "Dancing Script", "Brush Script MT", cursive;
    font-weight: 500;
    font-size: 24px;
    line-height: 1;
    color: var(--ink);
  }
  .person {
    position: absolute;
    left: 0;
    right: 0;
    top: 168px;
    text-align: center;
    font-family: "Dancing Script", "Brush Script MT", cursive;
    font-weight: 500;
    font-size: 90px;
    line-height: 1.1;
    color: var(--ink);
  }
  .contact {
    position: absolute;
    left: 46px;
    top: 368px;
    list-style: none;
    font-size: 14px;
    line-height: 22px;
    color: var(--ink-soft);
  }
  .contact__label {
    font-weight: 600;
    color: var(--ink);
  }
  .website {
    position: absolute;
    right: 26px;
    top: 416px;
    font-size: 13px;
    letter-spacing: 0.3px;
    color: var(--ink-soft);
  }
</style>
</head>
<body>
  <main class="sheet">
    <section class="card card--front" aria-label="Card front">
      <div class="brand">
        <span class="brand__dot" aria-hidden="true"></span>
        <span class="brand__name">Tarvello Studios</span>
      </div>
      <p class="tagline">EVENTS &amp; ENTERTAINMENT MANAGEMENT</p>
    </section>

    <section class="card card--back" aria-label="Card back">
      <p class="brand-mini">Tarvello Studios</p>
      <h1 class="person">Wren Hollis</h1>
      <ul class="contact">
        <li><span class="contact__label">m:</span> 0487 552 031</li>
        <li><span class="contact__label">e:</span> wren@tarvellostudios.com.au</li>
        <li><span class="contact__label">f</span> Tarvello Studios</li>
      </ul>
      <p class="website">www.tarvellostudios.com.au</p>
    </section>
  </main>
</body>
</html>
```